Redesign website for small print company

Vindaborgprent is a small printing company in Iceland mainly servicing Students, schools, etc. We are also doing all kind of other jobs, like business cards, book printing, brochure printing etc. We are also selling books online.
Our website is: www.vindaborgprent.is
What we are looking for is:
- Web Design (Uncoded - PSD layout only)
- Mobile friendly design, using our current color scheme: Red, green, yellow and light gray.
- Clean simple design
- Simple, light and easy to use.
- More menu Items/drop down
Industry/Entity Type
Digital Printing
Number of Pages Required
5+ page
Requirements
Must have
- Easy navigation
- Designed for mobile
- Current color scheme (see logo)
Nice to have
- Icon based products

```html
<!DOCTYPE html>
<html lang="en">
<head>
<meta charset="utf-8">
<title>Vindaborgprent – Printing Services</title>
<link rel="stylesheet" href="https://fonts.googleapis.com/css2?family=Montserrat:wght@400;500;600;700;800&family=Arimo:wght@400;700&display=swap">
<style>
:root{
  --yellow:#ffd400;
  --yellow-soft:#ffe23d;
  --black:#111111;
  --ink:#1d1d1d;
  --grey:#5d5d5d;
  --light:#f3f3f3;
  --white:#ffffff;
  --red:#e3262b;
  --green:#2f9a3c;
}
*{box-sizing:border-box;margin:0;padding:0}
html,body{width:1200px;height:3120px;overflow:hidden}
body{font-family:"Arimo",Arial,sans-serif;color:var(--ink);background:var(--white);position:relative}
.abs{position:absolute}

/* top bar */
.topbar{top:0;left:0;width:1200px;height:38px;background:var(--light);font-size:12px;font-family:"Montserrat",sans-serif}
.topbar .phone{left:30px;top:11px;display:flex;gap:8px;align-items:center}
.topbar .links{right:30px;top:11px;display:flex;gap:34px}
.topbar .links span{display:flex;gap:8px;align-items:center}

/* header */
.header{top:38px;left:0;width:1200px;height:112px;background:var(--white)}
.brand{left:24px;top:34px;display:flex;align-items:center;gap:10px;font-family:"Montserrat",sans-serif;font-weight:700;font-size:30px;color:var(--black)}
.brand .mark{width:38px;height:38px;background:var(--red)}
.nav{right:0;top:0;height:112px;display:flex;font-family:"Montserrat",sans-serif;font-weight:600;font-size:15px}
.nav a{display:flex;align-items:center;padding:0 22px;color:var(--black);text-decoration:none}
.nav a.active{background:var(--yellow);padding:0 20px}

/* hero */
.hero{top:150px;left:0;width:1200px;height:590px;overflow:hidden}
.hero-photo{inset:0;background:linear-gradient(120deg,#6d6d6d 0%,#3a3a3a 45%,#1f1f1f 100%)}
.hero-person{left:700px;top:0;width:440px;height:590px;background:linear-gradient(180deg,#b9b9b9 0%,#7d8591 40%,#4d5562 100%);border-radius:180px 180px 0 0}
.hero h1{left:24px;top:118px;font-family:"Montserrat",sans-serif;font-weight:600;font-size:40px;line-height:46px}
.hero h1 span{display:inline-block;padding:0 6px;background:var(--white);color:var(--black);margin-bottom:2px;line-height:44px}
.hero h1 span.accent{background:var(--black);color:var(--yellow);margin-left:-6px}
.hero .lead{left:26px;top:232px;width:660px;font-family:"Montserrat",sans-serif;font-weight:600;font-size:15px;line-height:21px;color:var(--black)}
.btn-order{left:24px;top:302px;width:148px;height:36px;background:var(--white);font-family:"Montserrat",sans-serif;font-weight:600;font-size:13px;display:flex;align-items:center;justify-content:center;box-shadow:4px 4px 0 rgba(0,0,0,.35)}
.partners{left:80px;top:535px;display:flex;gap:26px}
.partners i{display:block;width:46px;height:28px;background:rgba(255,255,255,.35);border-radius:4px}

/* about */
.about-tag{left:124px;top:895px;transform:rotate(-90deg);transform-origin:left top;font-size:11px;color:var(--yellow);font-weight:700;letter-spacing:1px;white-space:nowrap}
.about h2{left:158px;top:812px;font-family:"Montserrat",sans-serif;font-weight:700;font-size:32px}
.about .intro{left:158px;top:857px;width:490px;font-size:11px;line-height:14px;color:var(--grey)}
.about .body{left:158px;top:912px;width:480px;font-size:14px;line-height:17px}
.stats{left:158px;top:1030px;display:flex;gap:13px}
.stat{width:110px;height:128px;background:var(--black);color:var(--white);display:flex;flex-direction:column;align-items:center;padding-top:14px;font-family:"Montserrat",sans-serif}
.stat .num{width:70px;height:70px;border-radius:50%;background:var(--yellow);display:flex;align-items:center;justify-content:center;font-weight:800;font-size:30px;color:var(--white);text-shadow:0 0 2px #000,0 0 2px #000}
.stat .lbl{font-size:11px;font-weight:600;text-align:center;line-height:13px;margin-top:6px}
.machine-frame{left:858px;top:868px;width:206px;height:256px;border:10px solid var(--black)}
.machine{left:740px;top:900px;width:300px;height:210px;background:linear-gradient(160deg,#e9e9e9,#9a9a9a);border-radius:10px}

/* featured */
.featured-band{top:1230px;left:0;width:1200px;height:605px}
.featured h2{left:0;width:1200px;top:1385px;text-align:center;font-family:"Montserrat",sans-serif;font-weight:700;font-size:34px;color:var(--black)}
.featured .sub{left:360px;width:480px;top:1428px;text-align:center;font-size:12px;line-height:14px;color:#333}
.products{left:205px;top:1505px;display:flex;gap:102px}
.product{width:116px;display:flex;flex-direction:column;align-items:center;text-align:center}
.product .icon{width:116px;height:116px;border-radius:50%;background:var(--black);display:flex;align-items:center;justify-content:center}
.product h3{font-size:17px;line-height:21px;margin-top:14px;color:var(--black);width:120px}
.product p{font-size:11px;line-height:13px;width:180px;margin-top:8px;color:#222}
.product .more{margin-top:10px;background:var(--black);color:var(--white);font-size:10px;font-weight:700;padding:5px 10px;border-radius:3px}

/* press */
.press-tri{top:1835px;left:0}
.devices{left:150px;top:2025px;width:350px;height:300px;background:linear-gradient(135deg,#cfd4da,#5f6670);border-radius:18px}
.press h2{left:578px;top:1908px;font-family:"Arimo",sans-serif;font-weight:700;font-size:38px;color:var(--black)}
.press .sub{left:580px;top:1952px;width:390px;font-size:12px;line-height:14px;color:#333}
.post{left:578px;width:560px;height:200px}
.post .no{position:absolute;left:0;top:-2px;font-family:"Arimo",sans-serif;font-size:38px;color:#8a8a8a}
.post h3{position:absolute;left:50px;top:2px;border-left:3px solid var(--black);padding-left:8px;font-family:"Arimo",sans-serif;font-weight:700;font-size:26px;line-height:23px;color:var(--black);white-space:nowrap}
.post .date{position:absolute;left:58px;top:52px;font-size:14px;color:var(--grey)}
.post p{position:absolute;left:58px;top:76px;width:440px;font-size:17px;line-height:21px}
.post .read{position:absolute;left:58px;top:148px;font-size:14px;font-weight:700;display:flex;gap:8px;align-items:center}
.post .read b{color:var(--yellow)}

/* cta */
.cta h2{left:0;width:1200px;top:2535px;text-align:center;font-family:"Arimo",sans-serif;font-weight:700;font-size:32px;color:var(--black)}
.cta p{left:0;width:1200px;top:2577px;text-align:center;font-size:16px;font-weight:700;color:#555}
.cta .btn{left:413px;top:2612px;width:356px;height:44px;border-radius:8px;background:linear-gradient(180deg,#ffd84a,#f7a21b);display:flex;align-items:center;justify-content:center;font-family:"Arimo",sans-serif;font-weight:700;font-size:22px;color:var(--black)}

/* footer */
.footer{top:2728px;left:0;width:1200px;height:392px;background:linear-gradient(180deg,#2a2a2a,#141414 70%,#0d0d0d);color:var(--white)}
.footer .col{top:38px;height:260px}
.footer .sep{top:40px;width:1px;height:255px;background:rgba(255,255,255,.2)}
.footer h4{font-family:"Arimo",sans-serif;font-weight:700;font-size:21px;line-height:24px}
.footer ul{list-style:none;font-size:16px;font-weight:700;line-height:21px}
.footer .f-brand{left:38px;top:232px;display:flex;gap:8px;align-items:center;font-family:"Montserrat",sans-serif;font-weight:700;font-size:20px;color:#8a8a8a}
.footer .f-brand i{display:block;width:24px;height:24px;background:#8a8a8a}
.social{display:flex;gap:8px;margin-top:22px}
.social i{display:block;width:32px;height:32px;border-radius:50%;background:#4a6fb5}
.footer .office{right:38px;text-align:right}
.footer .copy{left:0;width:1200px;top:338px;text-align:center;font-size:14px;font-weight:700}
.footer .rule{left:38px;top:318px;width:1124px;height:1px;background:rgba(255,255,255,.2)}
</style>
</head>
<body>

<div class="abs topbar">
  <div class="abs phone">
    <svg width="14" height="14" viewBox="0 0 24 24"><path d="M6.6 10.8a15.2 15.2 0 0 0 6.6 6.6l2.2-2.2c.3-.3.7-.4 1-.2 1.1.4 2.3.6 3.6.6.6 0 1 .4 1 1V20c0 .6-.4 1-1 1A17 17 0 0 1 3 4c0-.6.4-1 1-1h3.5c.6 0 1 .4 1 1 0 1.3.2 2.5.6 3.6.1.3 0 .7-.2 1z" fill="#111"/></svg>
    Questions? Call us. 555.010.2040
  </div>
  <div class="abs links">
    <span><svg width="18" height="14" viewBox="0 0 18 14"><path d="M1 6l5-4 3 3 3-3 5 4-5 5-3-2-3 2z" fill="#111"/></svg>Place an order</span>
    <span><svg width="16" height="16" viewBox="0 0 16 16"><path d="M15 1L6 6 2 6 1 8 5 9 7 13 9 12 9 9z" fill="#111"/></svg>Send Files</span>
    <span><svg width="14" height="16" viewBox="0 0 14 16"><rect x="1" y="1" width="12" height="14" fill="none" stroke="#111" stroke-width="2"/><path d="M4 5h6M4 8h6M4 11h4" stroke="#111" stroke-width="1.5"/></svg>Request An Estimate</span>
    <span><svg width="16" height="12" viewBox="0 0 16 12"><rect x="0" y="0" width="16" height="12" fill="#111"/><path d="M0 0l8 6 8-6" stroke="#fff" fill="none"/></svg>Contact us</span>
  </div>
</div>

<header class="abs header">
  <div class="abs brand"><span class="mark"></span>VINDABORGPRENT</div>
  <nav class="abs nav">
    <a class="active" href="#">HOME</a>
    <a href="#">OUR COMPANY</a>
    <a href="#">OUR SERVICES</a>
    <a href="#">PRODUCTS</a>
    <a href="#">EMPLOYMENT</a>
  </nav>
</header>

<section class="abs hero">
  <div class="abs hero-photo" role="img" aria-label="Desk with a keyboard and printed papers"></div>
  <svg class="abs" style="left:0;top:0" width="1200" height="590"><polygon points="0,0 660,0 210,590 0,590" fill="var(--yellow)"/><polygon points="660,0 760,0 300,590 210,590" fill="rgba(0,0,0,.15)"/></svg>
  <div class="abs hero-person" role="img" aria-label="Smiling businessman in a grey suit giving a thumbs up"></div>
  <h1 class="abs"><span>LET US HANDLE</span><br><span>YOUR DOCUMENT</span><span class="accent">SOLUTIONS</span></h1>
  <p class="abs lead">Lorem ipsum dolor sit amet, consectetur adipiscing elit, sed do eiusmod tempor incididunt ut labore et dolore magna aliqua</p>
  <div class="abs btn-order">ORDER NOW</div>
  <div class="abs partners"><i></i><i></i><i></i><i></i><i></i><i></i></div>
</section>

<section class="about">
  <div class="abs about-tag">SINCE 1983</div>
  <h2 class="abs">Proudly serving the local area</h2>
  <p class="abs intro">Home of the "$.35 Color Copies" and located in the Old Harbour District of downtown Vindaborg, we provide graphic design and print services for business, personal, school and decor.</p>
  <p class="abs body">From banners to business cards, our design team and printing experts are here to make your project one-of-a-kind. Our customer centric commitment was how we began our company 30 years ago and the same principles apply today. We'll work with you every step and are committed to exceeding your expectations.</p>
  <div class="abs stats">
    <div class="stat"><div class="num">70%</div><div class="lbl">PROJECT<br>COMPLETED</div></div>
    <div class="stat"><div class="num">50%</div><div class="lbl">PROJECT<br>COMPLETED</div></div>
    <div class="stat"><div class="num">70%</div><div class="lbl">PROJECT<br>COMPLETED</div></div>
    <div class="stat"><div class="num">70%</div><div class="lbl">PROJECT<br>COMPLETED</div></div>
  </div>
  <div class="abs machine-frame"></div>
  <div class="abs machine" role="img" aria-label="Offset printing press machine"></div>
</section>

<section class="featured">
  <svg class="abs featured-band" width="1200" height="605"><defs><linearGradient id="fy" x1="0" y1="0" x2="0" y2="1"><stop offset="0" stop-color="var(--yellow-soft)"/><stop offset="1" stop-color="var(--yellow)"/></linearGradient></defs><polygon points="0,130 1200,0 1200,605 0,605" fill="url(#fy)"/></svg>
  <h2 class="abs">OUR FEATURED PRODUCTS</h2>
  <p class="abs sub">Lorem ipsum dolor sit amet, consectetur adipiscing elit, sed do eiusmod tempor incididunt ut labore et dolore magna aliqua</p>
  <div class="abs products">
    <div class="product">
      <div class="icon"><svg width="64" height="64" viewBox="0 0 64 64"><rect x="18" y="8" width="28" height="18" fill="#fff"/><rect x="8" y="24" width="48" height="22" rx="3" fill="var(--yellow)"/><rect x="18" y="38" width="28" height="20" fill="#fff"/><path d="M22 44h20M22 50h20" stroke="#111" stroke-width="2"/></svg></div>
      <h3>High Quality Printing</h3>
      <p>Lorem ipsum dolor sit amet, consectetur adipiscing elit, sed do eiusmod tempor incididunt</p>
      <span class="more">SEE MORE</span>
    </div>
    <div class="product">
      <div class="icon"><svg width="64" height="64" viewBox="0 0 64 64"><rect x="6" y="14" width="52" height="36" fill="var(--yellow)"/><path d="M6 14l26 20 26-20M6 50l20-18M58 50L38 32" stroke="#111" stroke-width="3" fill="none"/></svg></div>
      <h3>Envelope Printing</h3>
      <p>Lorem ipsum dolor sit amet, consectetur adipiscing elit, sed do eiusmod tempor incididunt</p>
      <span class="more">SEE MORE</span>
    </div>
    <div class="product">
      <div class="icon"><svg width="64" height="64" viewBox="0 0 64 64"><rect x="14" y="8" width="36" height="48" fill="var(--yellow)"/><circle cx="32" cy="26" r="8" fill="#111"/><path d="M22 42h20M22 48h14" stroke="#111" stroke-width="2"/></svg></div>
      <h3>Postcard Printing</h3>
      <p>Lorem ipsum dolor sit amet, consectetur adipiscing elit, sed do eiusmod tempor incididunt</p>
      <span class="more">SEE MORE</span>
    </div>
    <div class="product">
      <div class="icon"><svg width="64" height="64" viewBox="0 0 64 64"><rect x="18" y="8" width="28" height="18" fill="#fff"/><rect x="8" y="24" width="48" height="22" rx="3" fill="var(--yellow)"/><rect x="18" y="38" width="28" height="20" fill="#fff"/><path d="M22 44h20M22 50h20" stroke="#111" stroke-width="2"/></svg></div>
      <h3>High Quality Printing</h3>
      <p>Lorem ipsum dolor sit amet, consectetur adipiscing elit, sed do eiusmod tempor incididunt</p>
      <span class="more">SEE MORE</span>
    </div>
  </div>
</section>

<section class="press">
  <svg class="abs press-tri" width="600" height="590"><polygon points="0,0 590,0 0,565" fill="var(--black)"/></svg>
  <div class="abs devices" role="img" aria-label="Tablet and smartphone showing analytics charts"></div>
  <h2 class="abs">HOT OFF THE PRESS</h2>
  <p class="abs sub">Lorem ipsum dolor sit amet, consectetur adipiscing elit, sed do eiusmod tempor incididunt ut labore et dolore magna aliqua</p>
  <article class="abs post" style="top:2022px">
    <span class="no">01</span>
    <h3>HOW TO WRITE A SMALL BUSINESS<br>NEWSLETTER</h3>
    <span class="date">October 8, 2018</span>
    <p>Fortunately, there are some tips out there to help you write a powerful newsletter in order to connect with customers, promote the brand and grow the business.</p>
    <span class="read"><b>&gt;&gt;</b>Continue Reading</span>
  </article>
  <article class="abs post" style="top:2232px">
    <span class="no">02</span>
    <h3>HOW TO WRITE A SMALL BUSINESS<br>NEWSLETTER</h3>
    <span class="date">October 8, 2018</span>
    <p>Fortunately, there are some tips out there to help you write a powerful newsletter in order to connect with customers, promote the brand and grow the business.</p>
    <span class="read"><b>&gt;&gt;</b>Continue Reading</span>
  </article>
</section>

<section class="cta">
  <h2 class="abs">WANT TO IMPROVE YOUR ROI? LET'S TALK</h2>
  <p class="abs">We'll never turn down an opportunity to discover how we can help grow your business.</p>
  <div class="abs btn">CONTACT US TODAY</div>
</section>

<footer class="abs footer" role="img" aria-label="Night city skyline behind the footer">
  <div class="abs col" style="left:38px">
    <h4>Our Key Services</h4>
    <ul style="margin-top:18px"><li>Link Outreach</li><li>Organic Search (SEO)</li><li>Paid Search (PPC)</li><li>Social Media Marketing</li></ul>
  </div>
  <div class="abs f-brand"><i></i>VINDABORGPRENT</div>
  <div class="abs sep" style="left:248px"></div>
  <div class="abs col" style="left:290px">
    <h4>Locations We Cover<br>(SEO)</h4>
    <ul style="margin-top:12px"><li>Birmingham</li><li>Essex</li><li>London</li><li>Manchester</li><li>Stoke-on-Trent</li><li>&raquo;&nbsp; See All Locations We Cover</li></ul>
  </div>
  <div class="abs sep" style="left:600px"></div>
  <div class="abs col" style="left:652px">
    <h4>Connect With Us</h4>
    <div class="social"><i></i><i style="background:#3fa3e0"></i><i style="background:#d34836"></i><i style="background:#2a6fb0"></i><i style="background:#d9322b"></i></div>
  </div>
  <div class="abs sep" style="left:872px"></div>
  <div class="abs col office">
    <h4>Kestleford Office</h4>
    <ul style="margin-top:18px"><li>Northbay Media Ltd, The Granary</li><li>14 Elmstead Rd, Marrow Hill</li><li>Kestleford</li><li>KT4 2QB</li></ul>
    <ul style="margin-top:28px"><li>Phone: 01632 960418</li><li>Email: hello@northbaymedia.com</li></ul>
  </div>
  <div class="abs rule"></div>
  <div class="abs copy">© 2018 Vindaborgprent. All rights reserved.</div>
</footer>

</body>
</html>
```